Flyer-Design für Vermittlung von Immobilien
Zielgruppe
Immobilien vermitteln, für Käufer und Verkäufer, für Mieter und Vermieter
Aufgabenstellung
Inhalt Seite 1: Wir verkaufen Ihr Grundstück, Ihr Haus, Ihre Wohnung
Inhalt Seite 2: Wir suchen für solvente Kunden Ihr Grundstück, Ihr Haus, Ihre Wohnung
Weiterhin soll das Design in Anlehnung der DOLKAN Visitenkarte (siehe vorhergehendes Projekt) layoutet werden. Die Kontakte sollen explizit auf einen Makler mit Foto verweisen.

```html
<!DOCTYPE html>
<html lang="de">
<head>
<meta charset="utf-8">
<title>DOLKAN Immobilien – Flyer</title>
<link href="https://fonts.googleapis.com/css2?family=Rubik:wght@400;500;700&display=swap" rel="stylesheet">
<style>
  :root{
    --navy:#132846;
    --navy-light:#3a4b6c;
    --ink:#14233f;
    --white:#ffffff;
    --page:#ffffff;
    --photo-sky:#a9c3d8;
    --photo-green:#6d8f3e;
    --photo-stone:#c9c6bd;
    --photo-suit:#5d6f8a;
    --photo-table:#b9a58c;
    --portrait:#c8c4bd;
  }
  *{margin:0;padding:0;box-sizing:border-box}
  html,body{width:1200px;height:1118px;overflow:hidden;background:var(--page);font-family:'Rubik',sans-serif;color:var(--ink)}
  .flyer{position:absolute;top:65px;width:501px;height:992px;overflow:hidden;
    background:linear-gradient(100deg,var(--navy-light) 0%,var(--navy) 28%,var(--navy) 100%);
    box-shadow:0 6px 28px rgba(0,0,0,.18)}
  .flyer--front{left:65px}
  .flyer--back{left:646px}
  .photo{position:absolute;left:0;top:0;width:100%}
  .photo--street{height:609px;background:linear-gradient(180deg,var(--photo-sky) 0%,#d9dcd8 30%,var(--photo-stone) 55%,var(--photo-green) 78%,#8aa45a 100%)}
  .photo--handshake{height:333px;background:linear-gradient(160deg,var(--photo-suit) 0%,#8d97a6 40%,var(--photo-table) 75%,#6e5e4c 100%)}
  .cta-band{position:absolute;left:0;top:609px;width:100%;height:54px;background:var(--white);
    display:flex;align-items:center;justify-content:center;font-size:20px;font-weight:400}
  .cta-band strong{font-weight:700;margin-right:6px}
  .bubble{position:absolute;background:var(--white);text-align:center;box-shadow:0 2px 6px rgba(0,0,0,.15);
    display:flex;flex-direction:column;justify-content:center}
  .bubble .tail{position:absolute;overflow:visible}
  .bubble h2{font-weight:700;line-height:1.2}
  .bubble p{font-weight:700;font-size:20px;line-height:1.35;margin-top:8px}
  .bubble--search{left:40px;top:30px;width:353px;height:173px}
  .bubble--search h2{font-size:31px}
  .bubble--sell{left:111px;top:406px;width:350px;height:145px}
  .bubble--sell h2{font-size:32px}
  .bubble--partner{left:76px;top:288px;width:353px;height:118px}
  .bubble--partner h2{font-size:21px;line-height:1.3}
  .portrait{position:absolute;left:187px;top:443px;width:115px;height:151px;
    background:linear-gradient(180deg,#dcd9d3 0%,var(--portrait) 60%,#6f7684 100%)}
  .agent{position:absolute;left:0;top:612px;width:100%;text-align:center;color:var(--white)}
  .agent__name{font-weight:700;font-size:17px}
  .agent__role{font-weight:400;font-size:16px;margin-top:3px}
  .brand{position:absolute;left:0;top:800px;width:100%;text-align:center;color:var(--white)}
  .brand__name{font-size:27px;font-weight:500;letter-spacing:17px;padding-left:17px}
  .brand__sub{font-size:12px;font-weight:500;letter-spacing:6px;padding-left:6px;margin-top:6px}
  .contact{position:absolute;left:0;top:895px;width:100%;text-align:center;color:var(--white);font-weight:700;font-size:16px;line-height:21px}
  .contact .web{margin-top:5px;display:block}
</style>
</head>
<body>

<section class="flyer flyer--front">
  <div class="photo photo--street" role="img" aria-label="Foto: moderne Wohnhäuser mit Hecken, Bäumen und Blumenbeet an einem sonnigen Gehweg"></div>

  <div class="bubble bubble--search">
    <h2>Wir suchen für<br>solvente Kunden</h2>
    <p>Ihr Grundstück, Ihr Haus,<br>Ihre Wohnung!</p>
    <svg class="tail" style="left:0;top:0" width="353" height="250"><polygon points="14,173 79,173 81,215" fill="#fff"/></svg>
  </div>

  <div class="bubble bubble--sell">
    <h2>Wir verkaufen</h2>
    <p>Ihr Grundstück, Ihr Haus,<br>Ihre Wohnung!</p>
    <svg class="tail" style="left:0;top:0" width="350" height="200"><polygon points="274,145 322,145 269,188" fill="#fff"/></svg>
  </div>

  <div class="cta-band"><strong>Rufen Sie uns an!</strong> Wir beraten Sie gerne.</div>

  <div class="brand">
    <div class="brand__name">DOLKAN</div>
    <div class="brand__sub">IMMOBILIEN</div>
  </div>
  <div class="contact">
    +49 (0) 170 5 42 17 63<br>
    l.berger@dolkan.immo
    <span class="web">www.dolkan.immo</span>
  </div>
</section>

<section class="flyer flyer--back">
  <div class="photo photo--handshake" role="img" aria-label="Foto: Händedruck zweier Geschäftsleute über einem Tisch mit Kaffeetasse"></div>

  <div class="bubble bubble--partner">
    <h2>Wir sind Ihr kompetenter<br>Partner im Bereich Kauf und<br>Verkauf von Immobilien.</h2>
    <svg class="tail" style="left:0;top:0" width="353" height="170"><polygon points="278,118 322,118 272,160" fill="#fff"/></svg>
  </div>

  <div class="portrait" role="img" aria-label="Porträtfoto der Immobilienberaterin"></div>
  <div class="agent">
    <div class="agent__name">Laura Berger</div>
    <div class="agent__role">Meister(in) / Immobilienberatung</div>
  </div>

  <div class="brand">
    <div class="brand__name">DOLKAN</div>
    <div class="brand__sub">IMMOBILIEN</div>
  </div>
  <div class="contact">
    +49 (0) 170 5 42 17 63<br>
    l.berger@dolkan.immo
    <span class="web">www.dolkan.immo</span>
  </div>
</section>

</body>
</html>
```